hollowmere crest website

We need a new website for our new business division. We are a sustainable design firm specializing in servicing the needs if architects and developers. We have a staff consisting of architects, engineers, and former contractors and we understand green must make sense.

Bottomline - the only sustainable and hollowmere crest solutions are those thatbare good for the environment and good for our clients bottom line.

Our company is hollowmere crest and we will send you a copy of our logo you will see our tagline. Is simple. sustainable. solutions. The play with the periods is that we believe their are simple sustainable solutions and we want to use the words together and possible let each stand alone to accentuate their individual meaning in regards to benefit to our clients.

We want a cool splash page with nich graphics and pictures then later pages to feature projects and design ideas.

Target Market(s)

Our target customers are architects, developers, and contractors who would need assistance with the design process for a OVRA project or assisatnce with a building owner who wants to make tehir facilty more environmentally friendly and save energy costs at the same tiem.

Industry/Entity Type

Environment

Requirements
Must have
• Needs a construction look with an environmentally friendly surrounding that is pleasing to look at. Must appeal to the client not only as environmentally friendly but also a wise investment.
Nice to have
• Opportunity for a connection to Social networking including a blog.
Should not have
• A totally environmental building feel at whatever cost. We want to emphasize that it is possible to build environmental friendly and save you money over the life of your building

```html
<!DOCTYPE html>
<html lang="en">
<head>
<meta charset="utf-8">
<title>hollowmere crest</title>
<link rel="stylesheet" href="https://fonts.googleapis.com/css2?family=Arimo:wght@400;700&family=Open+Sans:wght@400;600&display=swap">
<style>
:root{
  --leaf-light:#c9e05a;
  --leaf-mid:#8dbb2a;
  --brand-green:#3f8f2c;
  --accent-green:#6aa82a;
  --dot-yellow:#c7d21c;
  --ink:#5f5f5f;
  --ink-soft:#8a8a8a;
  --rule:#c9c9c9;
  --nav-dark:#1e1e1e;
  --nav-light:#3a3a3a;
  --footer-top:#2e2e2e;
  --footer-bottom:#171717;
  --white:#ffffff;
}
*{margin:0;padding:0;box-sizing:border-box}
html,body{width:1200px;height:1062px;overflow:hidden;background:var(--white)}
body{position:relative;font-family:"Open Sans",Arial,sans-serif;color:var(--ink)}
.abs{position:absolute}

.hero-backdrop{left:0;top:0;width:1200px;height:560px;
  background:
    radial-gradient(ellipse 420px 520px at 80px 200px,var(--leaf-light),transparent 70%),
    radial-gradient(ellipse 360px 500px at 1130px 220px,var(--leaf-light),transparent 70%),
    linear-gradient(180deg,var(--leaf-mid) 0%,var(--leaf-light) 45%,#e9f2c8 75%,var(--white) 100%);}
.page-panel{left:0;top:0}

.brand{left:177px;top:36px;display:flex;align-items:center;gap:10px}
.brand-mark{width:42px;height:42px;border-radius:50%;background:var(--brand-green)}
.brand-name{font-size:27px;font-weight:600;color:var(--brand-green);letter-spacing:-.5px;line-height:1}

.main-nav{left:495px;top:26px;width:554px;height:52px;border-radius:7px;
  background:linear-gradient(180deg,var(--nav-light),var(--nav-dark));display:flex;
  box-shadow:0 2px 3px rgba(0,0,0,.3)}
.main-nav a{flex:1;display:flex;align-items:center;justify-content:center;color:var(--white);
  text-decoration:none;font-family:Arimo,Arial,sans-serif;font-weight:700;font-size:18px;
  border-left:1px solid #4a4a4a;box-shadow:inset 1px 0 0 #111}
.main-nav a:first-child{border-left:0;box-shadow:none}

.slider{left:171px;top:120px;width:858px;height:398px;overflow:hidden;
  background:linear-gradient(90deg,#4b4f55 0%,#5a5e64 25%,#3c3f44 50%,#26282b 75%,#111 100%)}
.slider-photo{position:absolute;inset:0;
  background:linear-gradient(180deg,rgba(255,255,255,.08) 0%,transparent 40%,rgba(0,0,0,.55) 100%)}
.slider-arrow{position:absolute;width:68px;height:68px;border-radius:50%;
  background:radial-gradient(circle at 40% 35%,#9a9a9a,#5c5c5c);}
.slider-arrow svg{width:68px;height:68px}
.slider-dots{position:absolute;left:20px;top:364px;display:flex;gap:4px}
.slider-dots span{width:22px;height:22px;border-radius:50%;background:var(--dot-yellow)}
.slider-dots span.is-active{background:var(--brand-green)}

.feature{top:552px;width:260px}
.feature h2{font-weight:400;font-size:39px;color:var(--ink);line-height:1;letter-spacing:-.5px}
.feature p,.feature li{font-size:13.4px;line-height:17.2px;color:var(--ink-soft);white-space:nowrap}
.feature ul{list-style:none;margin-top:21px}
.feature li{position:relative;padding-left:17px;margin-bottom:5.3px}
.feature li::before{content:"";position:absolute;left:0;top:4px;border-left:10px solid var(--brand-green);
  border-top:4.5px solid transparent;border-bottom:4.5px solid transparent}
.feature p{margin-top:21px}
.divider{top:559px;width:2px;height:172px;background:var(--rule)}
.read-more{width:133px;height:33px;border-radius:6px;top:730px;
  background:linear-gradient(180deg,#3b3b3b,#111);color:var(--white);font-family:Arimo,Arial,sans-serif;
  font-weight:700;font-size:15px;display:flex;align-items:center;justify-content:center;
  box-shadow:0 1px 2px rgba(0,0,0,.4)}

.site-footer{left:0;top:798px;width:1200px;height:264px;
  background:linear-gradient(180deg,var(--footer-top),var(--footer-bottom))}
.footer-title{top:811px;font-family:Arimo,Arial,sans-serif;font-weight:700;font-size:16.5px;color:var(--accent-green)}
.footer-list{list-style:none}
.footer-list li{position:absolute;left:0;width:100%;font-size:12.5px;color:var(--white);
  padding-left:21px;border-bottom:1.5px dashed #d9d9d9;height:20px;line-height:16px}
.footer-list li.strong{font-weight:600}

.social{top:825px;display:flex;gap:5px;left:888px}
.social span{width:32px;height:32px;border-radius:4px;background:#6e6e6e}

.field-label{left:790px;font-family:Arimo,Arial,sans-serif;font-weight:700;font-size:10.5px;color:var(--accent-green)}
.field{left:790px;width:240px;background:var(--white);border:0}
.submit{left:945px;top:1025px;width:85px;height:22px;border-radius:4px;
  background:linear-gradient(180deg,#5fa32a,#3f7e17);color:var(--white);font-family:Arimo,Arial,sans-serif;
  font-weight:700;font-size:12px;display:flex;align-items:center;justify-content:center}
</style>
</head>
<body>

<div class="abs hero-backdrop" role="img" aria-label="Close-up photograph of a backlit green leaf with veins"></div>

<svg class="abs page-panel" width="1200" height="560" viewBox="0 0 1200 560" aria-hidden="true">
  <path d="M151 560 V28 Q151 3 176 3 H440 Q466 3 472 30 Q480 88 510 88 H1034 Q1049 88 1049 103 V560 Z" fill="#fff"/>
</svg>

<div class="abs brand" style="top:38px">
  <span class="brand-mark"></span>
  <span class="brand-name">hollowmere crest</span>
</div>

<nav class="abs main-nav">
  <a href="#">Home</a><a href="#">About Us</a><a href="#">Services</a><a href="#">Work</a><a href="#">Contact</a>
</nav>

<section class="abs slider">
  <div class="slider-photo" role="img" aria-label="Photograph of a modern dark grey house courtyard with a small tree in a gravel bed"></div>
  <div class="slider-arrow" style="left:21px;top:184px">
    <svg viewBox="0 0 68 68"><path d="M18 34 L46 21 L38 34 L46 47 Z" fill="#2a2a2a"/></svg>
  </div>
  <div class="slider-arrow" style="left:769px;top:184px">
    <svg viewBox="0 0 68 68"><path d="M50 34 L22 21 L30 34 L22 47 Z" fill="#2a2a2a"/></svg>
  </div>
  <div class="slider-dots"><span class="is-active"></span><span></span><span></span><span></span><span></span></div>
</section>

<section class="abs feature" style="left:167px">
  <h2 style="margin-left:62px">Simple</h2>
  <ul>
    <li>The point of using Lorem Ipsum is that it</li>
    <li>A more-or-less normal distribution of</li>
    <li>Here, content here', making it look like</li>
    <li>Many desktop publishing packages and</li>
    <li>Page editors now use Lorem Ipsum as</li>
  </ul>
</section>
<div class="abs divider" style="left:451px"></div>
<section class="abs feature" style="left:470px">
  <h2 style="margin-left:6px">Sustainable</h2>
  <p>Lorem Ipsum is simply dummy text of<br>the printing and typesetting<br>industry.Lorem Ipsum has been the<br>industry's standard dummy text ever<br>since the 1500s, when an<br>unknown printer took a galley of type</p>
</section>
<div class="abs divider" style="left:736px"></div>
<section class="abs feature" style="left:756px">
  <h2 style="margin-left:45px">Solution</h2>
  <p>Contrary to popular belief, Lorem Ipsum<br>is not simply random text. It has roots in<br>a piece of classical Latin literature from<br>45 BC, making it over 2000 years old.<br>Edwin Harrowgate, a Latin professor at<br>Ashcombe College</p>
</section>

<a class="abs read-more" style="left:303px">Read More »</a>
<a class="abs read-more" style="left:588px">Read More »</a>
<a class="abs read-more" style="left:897px">Read More »</a>

<footer class="abs site-footer"></footer>

<h3 class="abs footer-title" style="left:170px">Menu:</h3>
<ul class="abs footer-list" style="left:151px;top:0;width:279px">
  <li style="top:860px">Home</li>
  <li style="top:885px">About Us</li>
  <li style="top:910px">Services</li>
  <li style="top:935px">Work</li>
  <li style="top:959px">Gallery</li>
  <li style="top:988px">Blog</li>
  <li style="top:1015px">Contact</li>
</ul>

<h3 class="abs footer-title" style="left:479px">Partners:</h3>
<ul class="abs footer-list" style="left:459px;top:0;width:280px">
  <li style="top:859px">Discovered the undoubtable source.</li>
  <li style="top:885px">Content here, content here', making it</li>
  <li class="strong" style="top:910px">Contrary to popular belief</li>
  <li style="top:936px">Combined with a handful of model sentence</li>
  <li style="top:962px">Will uncover many web sites still</li>
  <li style="top:988px">Various versions have evolved over</li>
  <li class="strong" style="top:1014px">Contrary to popular belief</li>
</ul>

<h3 class="abs footer-title" style="left:784px">Contact Us:</h3>
<div class="abs social"><span></span><span></span><span></span><span></span></div>

<label class="abs field-label" style="top:868px">Name:</label>
<div class="abs field" style="top:884px;height:15px"></div>
<label class="abs field-label" style="top:903px">Email:</label>
<div class="abs field" style="top:915px;height:15px"></div>
<label class="abs field-label" style="top:934px">Coments:</label>
<div class="abs field" style="top:947px;height:70px"></div>
<div class="abs submit">Submit</div>

</body>
</html>
```